vantrel works cybersecurity website design and development

website design and development for a cybersecurity company. we have a logo and would like site to suit logo colors and look
cybersecurity website should be secure and look professional
main example of site we want to use: https://www.morvisquad.example/
site should be usable on tablet and phones

For each design proposal, please could you provide details of what language you'll use to code the website.

Target Market(s)

insurance companies, financial institutions, private SME, Africa and Europe

Coding

Coded - Design and coding required

Number of Pages Required

5+ page

Requirements
Must have
• 9 Pages:
Home
About us
Contacts
Partners
Blog
Services
( consulting, vulnerability assessment, information systems security audit, ISO compliance, Penetration testing, security awareness training, social engineering test, protection against DDoS, procurement )
Resources
Technologies
Careers
Nice to have
• nice to have all services have their own pages.
design based on logo colors and look

please provide what will be use to code the website

```html
<!DOCTYPE html>
<html lang="en">
<head>
<meta charset="utf-8">
<title>Vantrel Works — Cyber Security</title>
<link href="https://fonts.googleapis.com/css2?family=Poppins:wght@300;400;500;600;700&display=swap" rel="stylesheet">
<style>
:root{
  --navy:#0a1431;
  --navy-deep:#060c22;
  --blue:#1d4fb0;
  --blue-bright:#2f6fe0;
  --ink:#1b2438;
  --muted:#6b7385;
  --line:#dfe3ea;
  --grey-bg:#f1f2f5;
  --white:#ffffff;
}
*{box-sizing:border-box;margin:0;padding:0}
html,body{width:1200px;height:3644px;overflow:hidden}
body{font-family:"Poppins",sans-serif;color:var(--ink);background:var(--white);position:relative}
a{color:inherit;text-decoration:none}

/* header */
.site-header{position:absolute;top:0;left:0;width:1200px;height:80px;background:var(--white);display:flex;align-items:center;justify-content:space-between;padding:0 150px;z-index:2}
.brand{display:flex;align-items:center;gap:10px;font-weight:600;font-size:22px;color:var(--blue)}
.brand-mark{width:30px;height:30px;border-radius:50%;background:var(--blue)}
.main-nav{display:flex;gap:30px;font-size:14px;font-weight:500;color:var(--ink)}
.main-nav .active{color:var(--blue);border-bottom:2px solid var(--blue);padding-bottom:4px}

/* hero */
.hero{position:absolute;top:80px;left:0;width:1200px;height:700px;background:radial-gradient(circle at 72% 42%,#1e5cc4 0%,#0d2a6e 28%,#071539 60%,#040a1e 100%)}
.hero-copy{position:absolute;left:160px;top:210px;color:var(--white)}
.hero-kicker{font-size:20px;font-weight:300}
.hero-title{font-size:46px;line-height:1.2;font-weight:600;margin-top:6px}
.hero-actions{display:flex;gap:16px;margin-top:40px}
.btn{display:inline-block;font-size:11px;font-weight:600;letter-spacing:.5px;padding:11px 22px;border-radius:20px}
.btn-solid{background:var(--blue-bright);color:var(--white)}
.btn-outline{border:1.5px solid var(--white);color:var(--white)}
.slider-arrow{position:absolute;width:34px;height:34px;border-radius:50%;background:rgba(255,255,255,.85);display:flex;align-items:center;justify-content:center}
.scroll-cue{position:absolute;left:588px;width:22px;height:34px;border:2px solid rgba(255,255,255,.7);border-radius:12px}
.scroll-cue::after{content:"";position:absolute;left:8px;top:6px;width:3px;height:7px;background:rgba(255,255,255,.8);border-radius:2px}

/* about */
.about{position:absolute;top:780px;left:0;width:1200px;height:540px;background:var(--white)}
.section-label{font-size:14px;color:var(--blue);font-weight:500}
.about-copy{position:absolute;left:150px;top:130px;width:470px}
.about-title{font-size:26px;line-height:1.3;font-weight:700;color:var(--blue);margin-top:6px}
.about-text{font-size:12.5px;line-height:1.75;color:var(--muted);margin-top:16px}
.about-copy .btn{margin-top:28px;background:var(--blue);color:var(--white)}
.about-visual{position:absolute;left:740px;top:70px;width:220px;height:300px;border-radius:40px 40px 110px 110px;background:linear-gradient(160deg,#6d7b93 0%,#253659 45%,#0e1d45 100%);box-shadow:0 14px 30px rgba(10,20,49,.25)}

/* services */
.services{position:absolute;top:1320px;left:0;width:1200px;height:640px;background:var(--grey-bg)}
.section-head{position:absolute;left:0;width:1200px;text-align:center}
.eyebrow{display:inline-flex;align-items:center;gap:10px;font-size:11px;font-weight:600;letter-spacing:1px;color:var(--blue)}
.eyebrow::before,.eyebrow::after{content:"";width:30px;height:1px;background:var(--blue)}
.section-title{font-size:30px;font-weight:700;color:var(--navy);margin-top:2px;line-height:1.3}
.section-sub{font-size:12px;color:var(--muted);margin-top:2px}
.services-hub{position:absolute;left:462px;top:190px;width:276px;height:276px;border-radius:50%;background:radial-gradient(circle,#2f7be6 0%,#0f3b8c 45%,#081a44 100%);border:10px solid rgba(255,255,255,.7);box-shadow:0 0 0 1px var(--line)}
.service{position:absolute;width:300px}
.service h3{font-size:12px;font-weight:600;color:var(--navy);text-transform:uppercase;line-height:1.3}
.service p{font-size:10.5px;color:var(--muted);margin-top:2px}
.service.left{text-align:right}
.service-icon{position:absolute;width:34px;height:34px;border-radius:50%;background:var(--white);border:1.5px solid var(--line)}
.service-icon.featured{background:var(--blue);border-color:var(--blue)}

/* partners */
.partners{position:absolute;top:1960px;left:0;width:1200px;height:400px;background:var(--white)}
.partners-title{position:absolute;left:0;top:80px;width:1200px;text-align:center;font-size:32px;font-weight:400;color:var(--navy)}
.partners-title strong,.blog-title strong{font-weight:700}
.partner-row{position:absolute;left:130px;top:180px;width:940px;display:flex;justify-content:space-between;align-items:center}
.partner-badge{width:150px;height:70px;display:flex;align-items:center;justify-content:center}
.partner-badge.raised{background:var(--white);box-shadow:0 6px 20px rgba(10,20,49,.12)}
.badge-shape{width:110px;height:22px;border-radius:4px;background:#c9ced8}
.dots{position:absolute;left:0;top:328px;width:1200px;display:flex;justify-content:center;gap:7px}
.dots span{width:7px;height:7px;border-radius:50%;background:#c5cbd6}
.dots .on{background:var(--blue)}

/* cta */
.cta{position:absolute;top:2360px;left:0;width:1200px;height:320px;background:linear-gradient(100deg,#050b1d 0%,#0b1d4b 45%,#143a86 70%,#07102c 100%);color:var(--white);text-align:center;padding-top:74px}
.cta .eyebrow{color:var(--white)}
.cta .eyebrow::before,.cta .eyebrow::after{background:var(--white)}
.cta-title{font-size:30px;font-weight:600;margin-top:6px}
.cta-text{font-size:13px;font-weight:300;margin-top:4px}
.cta-actions{display:flex;justify-content:center;gap:16px;margin-top:26px}

/* blog */
.blog{position:absolute;top:2680px;left:0;width:1200px;height:520px;background:var(--white)}
.blog-title{position:absolute;left:0;top:58px;width:1200px;text-align:center;font-size:30px;font-weight:400;color:var(--navy)}
.blog-title::after{content:"";display:block;width:46px;height:3px;background:var(--blue);margin:8px auto 0}
.post{position:absolute;top:135px;width:270px;height:330px;background:var(--white);border:1px solid var(--line)}
.post.raised{box-shadow:0 10px 28px rgba(10,20,49,.15);border-color:transparent}
.post-media{height:168px;background:linear-gradient(135deg,#0c2a6b 0%,#2c6fd6 55%,#0a1842 100%)}
.post-body{padding:14px 18px}
.post-date{font-size:10px;color:var(--muted)}
.post-heading{font-size:14px;font-weight:500;color:var(--navy);line-height:1.35;margin-top:6px}
.post-text{font-size:10.5px;color:var(--muted);line-height:1.6;margin-top:8px}
.round-arrow{position:absolute;width:30px;height:30px;border-radius:50%;border:1.5px solid var(--blue);display:flex;align-items:center;justify-content:center}

/* footer */
.site-footer{position:absolute;top:3200px;left:0;width:1200px;height:444px;background:#181b22;color:#c9ccd3}
.footer-brand{position:absolute;left:150px;top:62px;display:flex;align-items:center;gap:10px;font-weight:600;font-size:22px;color:var(--white)}
.footer-brand .brand-mark{background:var(--blue-bright)}
.footer-h{font-size:13px;font-weight:600;color:var(--white);text-transform:uppercase;letter-spacing:.4px}
.footer-contact{position:absolute;left:150px;top:140px;width:230px}
.contact-line{display:flex;gap:10px;font-size:11px;line-height:1.5;margin-top:14px}
.quick-links{position:absolute;left:470px;top:64px}
.link-cols{display:flex;gap:70px;margin-top:16px}
.link-cols ul{list-style:none;font-size:11.5px;line-height:2}
.newsletter{position:absolute;left:780px;top:64px;width:270px}
.newsletter p{font-size:11px;line-height:1.55;margin-top:14px}
.subscribe{display:flex;margin-top:16px}
.subscribe input{flex:1;min-width:0;height:34px;background:#2a2e37;border:0;padding:0 12px;font-family:inherit;font-size:11px;color:#c9ccd3}
.subscribe button{height:34px;padding:0 16px;background:var(--blue-bright);color:var(--white);border:0;font-family:inherit;font-size:11px}
.socials{display:flex;gap:10px;margin-top:22px}
.socials span{width:26px;height:26px;border-radius:50%;border:1px solid #5a5f6b}
.footer-bottom{position:absolute;left:150px;top:400px;width:900px;display:flex;justify-content:space-between;font-size:10.5px;color:#8f94a0;border-top:1px solid #2c3039;padding-top:14px}
</style>
</head>
<body>

<header class="site-header">
  <a class="brand" href="#"><span class="brand-mark"></span>Vantrel Works</a>
  <nav class="main-nav">
    <a class="active" href="#">Home</a><a href="#">About</a><a href="#">Services</a><a href="#">Partners</a><a href="#">Blog</a><a href="#">Resources</a><a href="#">Contact Us</a>
  </nav>
</header>

<section class="hero" role="img" aria-label="Glowing digital security shield over a dark blue data-grid background">
  <div class="hero-copy">
    <p class="hero-kicker">The Right People For Your Team</p>
    <h1 class="hero-title">Cyber Thrieats and<br>Digitalisation Risks</h1>
    <div class="hero-actions">
      <a class="btn btn-solid" href="#">GET STARTED</a>
      <a class="btn btn-outline" href="#">LEARN MORE</a>
    </div>
  </div>
  <span class="slider-arrow" style="left:28px;top:315px"><svg width="12" height="12" viewBox="0 0 12 12"><path d="M8 2L4 6l4 4" stroke="#0a1431" stroke-width="2" fill="none"/></svg></span>
  <span class="slider-arrow" style="left:1138px;top:315px"><svg width="12" height="12" viewBox="0 0 12 12"><path d="M4 2l4 4-4 4" stroke="#0a1431" stroke-width="2" fill="none"/></svg></span>
  <span class="scroll-cue" style="top:620px"></span>
</section>

<section class="about">
  <div class="about-copy">
    <p class="section-label">About Us</p>
    <h2 class="about-title">LOREM IPSUM IS SIMPLY DUMMY TEXT OF THE PRINTING</h2>
    <p class="about-text">Lorem Ipsum is simply dummy text of the printing and typesetting industry. Lorem Ipsum has been the industry's standard dummy text ever since the 1500s, when an unknown printer took a galley of type and scrambled it to make a type specimen book. It has survived not only five centuries, but also the leap into electronic typesetting, remaining essentially unchanged.</p>
    <a class="btn" href="#">MORE ABOUT US</a>
  </div>
  <div class="about-visual" role="img" aria-label="Business professional inside a protective shield frame"></div>
</section>

<section class="services">
  <div class="section-head" style="top:46px">
    <span class="eyebrow">SERVICES</span>
    <h2 class="section-title">WHAT WE DO</h2>
    <p class="section-sub">Unparalleled Cyber Expertise Meets Exceptional Services</p>
  </div>
  <div class="services-hub" role="img" aria-label="Digital lock icon surrounded by glowing network lines"></div>

  <div class="service left" style="left:98px;top:180px"><h3>Consulting</h3><p>Lorem ipsum is simply dummy text</p></div>
  <span class="service-icon" style="left:412px;top:178px"></span>
  <div class="service left" style="left:98px;top:272px"><h3>Vulnerability Assessment</h3><p>Lorem ipsum is simply dummy text</p></div>
  <span class="service-icon" style="left:412px;top:270px"></span>
  <div class="service left" style="left:98px;top:372px"><h3>Information Systems<br>Security Audit</h3><p>Lorem ipsum is simply dummy text</p></div>
  <span class="service-icon" style="left:412px;top:374px"></span>
  <div class="service left" style="left:98px;top:478px"><h3>ISO Compliance</h3><p>Lorem ipsum is simply dummy text</p></div>
  <span class="service-icon" style="left:412px;top:476px"></span>

  <span class="service-icon" style="left:756px;top:178px"></span>
  <div class="service" style="left:802px;top:180px"><h3>Penetration Testing</h3><p>Lorem ipsum is simply dummy text</p></div>
  <span class="service-icon featured" style="left:756px;top:272px"></span>
  <div class="service" style="left:802px;top:266px"><h3 style="color:var(--blue)">Security Awareness<br>Training</h3><p>Lorem ipsum is simply dummy text</p></div>
  <span class="service-icon" style="left:756px;top:374px"></span>
  <div class="service" style="left:802px;top:376px"><h3>Social Engineering Test</h3><p>Lorem ipsum is simply dummy text</p></div>
  <span class="service-icon" style="left:756px;top:476px"></span>
  <div class="service" style="left:802px;top:478px"><h3>Protection Against DDoS</h3><p>Lorem ipsum is simply dummy text</p></div>
</section>

<section class="partners">
  <h2 class="partners-title">OUR <strong>PARTNERS</strong></h2>
  <div class="partner-row">
    <div class="partner-badge" aria-label="Quellis Secure"><span class="badge-shape"></span></div>
    <div class="partner-badge raised" aria-label="Nortagate"><span class="badge-shape"></span></div>
    <div class="partner-badge" aria-label="Brindle Systems"><span class="badge-shape"></span></div>
    <div class="partner-badge" aria-label="Halvex"><span class="badge-shape"></span></div>
    <div class="partner-badge" aria-label="Brindle Systems"><span class="badge-shape"></span></div>
  </div>
  <div class="dots"><span></span><span class="on"></span><span></span></div>
</section>

<section class="cta" role="img" aria-label="Close-up of a backlit keyboard in blue light">
  <span class="eyebrow">CONTACT</span>
  <h2 class="cta-title">READY TO LEARN MORE?</h2>
  <p class="cta-text">Contact us to discuss your upcoming IT security audit and compliance needs</p>
  <div class="cta-actions">
    <a class="btn btn-solid" href="#">CONTACT US</a>
    <a class="btn btn-outline" href="#">SCHEDULE A CALL</a>
  </div>
</section>

<section class="blog">
  <h2 class="blog-title">LATEST <strong>BLOG</strong></h2>
  <span class="round-arrow" style="left:96px;top:296px"><svg width="10" height="10" viewBox="0 0 12 12"><path d="M8 2L4 6l4 4" stroke="#1d4fb0" stroke-width="2" fill="none"/></svg></span>
  <span class="round-arrow" style="left:1074px;top:296px"><svg width="10" height="10" viewBox="0 0 12 12"><path d="M4 2l4 4-4 4" stroke="#1d4fb0" stroke-width="2" fill="none"/></svg></span>

  <article class="post" style="left:150px">
    <div class="post-media" role="img" aria-label="Cloud security graphic in blue"></div>
    <div class="post-body"><p class="post-date">AUG 20, 2021</p><h3 class="post-heading">Lorem Ipsum is simply dummy text of the printing industry.</h3><p class="post-text">Lorem Ipsum is simply dummy text of the printing and typesetting industry. Lorem Ipsum has been the industry's standard.</p></div>
  </article>
  <article class="post raised" style="left:465px">
    <div class="post-media" role="img" aria-label="Hand touching a digital security interface"></div>
    <div class="post-body"><p class="post-date">AUG 20, 2021</p><h3 class="post-heading">Lorem Ipsum is simply dummy text of the printing industry.</h3><p class="post-text">Lorem Ipsum is simply dummy text of the printing and typesetting industry. Lorem Ipsum has been the industry's standard.</p></div>
  </article>
  <article class="post" style="left:780px">
    <div class="post-media" role="img" aria-label="Padlock on a circuit board"></div>
    <div class="post-body"><p class="post-date">AUG 20, 2021</p><h3 class="post-heading">Lorem Ipsum is simply dummy text of the printing industry.</h3><p class="post-text">Lorem Ipsum is simply dummy text of the printing and typesetting industry. Lorem Ipsum has been the industry's standard.</p></div>
  </article>
</section>

<footer class="site-footer">
  <div class="footer-brand"><span class="brand-mark"></span>Vantrel Works</div>
  <div class="footer-contact">
    <h4 class="footer-h">Contact Us</h4>
    <p class="contact-line"><svg width="12" height="14" viewBox="0 0 12 14"><path d="M6 0a5 5 0 0 0-5 5c0 4 5 9 5 9s5-5 5-9a5 5 0 0 0-5-5z" fill="#2f6fe0"/><circle cx="6" cy="5" r="1.8" fill="#181b22"/></svg><span>2417 Lorem Ipsum Road, simply dummy text of the printing</span></p>
    <p class="contact-line"><svg width="12" height="12" viewBox="0 0 12 12"><path d="M2 1l2 0 1 3-1.3 1a7 7 0 0 0 3.3 3.3L8 7l3 1v2a1 1 0 0 1-1 1A9 9 0 0 1 1 2a1 1 0 0 1 1-1z" fill="#2f6fe0"/></svg><span>123 456 7890</span></p>
  </div>
  <div class="quick-links">
    <h4 class="footer-h">Quick Links</h4>
    <div class="link-cols">
      <ul><li>Home</li><li>About Us</li><li>Our Services</li><li>Partners</li><li>Blog</li></ul>
      <ul><li>Resources</li><li>Contact Us</li><li>Technologies</li><li>Careers</li><li>Sitemap</li></ul>
    </div>
  </div>
  <div class="newsletter">
    <h4 class="footer-h">Sign Up for Newsletter</h4>
    <p>If you are interested in joining our team, or have any questions please send us a message.</p>
    <div class="subscribe"><input type="text" placeholder="Email address"><button>Subscribe</button></div>
    <div class="socials"><span></span><span></span><span></span><span></span></div>
  </div>
  <div class="footer-bottom"><span>© 2021 Vantrel Works. All Rights Reserved.</span><span>Privacy Policy | Terms of Use</span></div>
</footer>

</body>
</html>
```